Design a Striking Charity Infographic for the Displaced Meal Pledge

Design a striking infographic to share online and raise awareness of the Meal Pledge.

This is a charity project that raises funds to provide refugees with the food, medicine and support they need to survive.

Your design should include the text and ingredients outlined below.

The infographic should be a strong visual statement that’s easy to share on social media such as Picstream, Chirpline and Friendwall.

The headline, ingredients and call to action 'Take the Hope Bridge Meal Pledge, June 19-25'

Text:
Headline: “Could you live on this much food for 1 week?”
Rice 1920g
Flour 400g
Lentils 170g
Dried chick peas 85g
Tinned sardines 125g
Tinned kidney beans 400g
Vegetable Oil 300ml

Take the Hope Bridge Meal Pledge, June 19-25
Sign up at www.mealpledge.example.org.au
(this section with the web address needs to be very clear and easy to see in the graphic)

Footer text - note this section should not dominate, it's a teriary section of the design.
(1) Hope Bridge / Meal Pledge logo
(2) Design by ArtHive (logo attached)

This copy needs to appear somewhere (very small) “The international aid agency of the United Assembly of Parishes. ABN 17 826 305 419”

Technical spec:
Imagery: photos are permitted; custom illustrations encouraged!
Size: maximum 1080x1080px
File size smaller than 5 MB
Colour ratios: Blue and White (80%), tertiary is red; see guide for more details

If the main image is full bleed you can stick headline copy, logos etc on top of it. Put body copy on a grunge brush.

If the images are not full bleed, use a blue background image (rice bag or paper) for the background. Put all the images in a frame. And fasten them on with a fastener (e.g. staple). Make the proportions of the frames / backgrounds / fasteners look realistic.

Logo:
Use the Meal Pledge stamp (larger) and Hope Bridge logo (smaller) on everything. Unless it’s on a plain white background use the sicker version of the HB logo.

Typography:
Veneer 2 for headlines
Caecelia is for body copy in print / on posters / on images put headline and body copy on a grunge brush
Remington Noiseless - use sparingly for personality elements, not for body copy

Pls read the Meal Pledge Visual identity guidelines attached

Background:
From the organizers: "The numbers of refugees are hard to get your head around. And that’s why you taking this challenge is so important.

By putting yourself in the shoes of just one refugee, for just one week, you’re helping to communicate the suffering caused by this crisis on a human level. At a level we, and those around us, can actually understand."

Extra assets:

Frames and fasteners and other assets can be found here: https://files.example-vault.com/s/q9mzt4kx2rbw8ndlpe6vyh3fc17jo5ua

Requirements
Must have
• Refer to the attached visual design guidelines pdf got the colour ratios

```html
<!DOCTYPE html>
<html lang="en">
<head>
<meta charset="utf-8">
<title>Meal Pledge – Could you live on this much food for 1 week?</title>
<link rel="stylesheet" href="https://fonts.googleapis.com/css2?family=Bebas+Neue&family=Cabin:wght@500;700&display=swap">
<style>
  :root {
    --red: #8c2a31;
    --paper: #f2f2f2;
    --sky: #5aa8db;
    --sky-deep: #3f8fc6;
    --navy: #175b8c;
    --ribbon: #1f6ba3;
    --ribbon-tail: #164f7c;
    --ink: #0f3f63;
    --white: #ffffff;
  }
  * { box-sizing: border-box; margin: 0; padding: 0; }
  html, body { width: 1200px; height: 1200px; overflow: hidden; background: #e6e6e6; }
  .poster { position: relative; width: 1200px; height: 1200px; background: var(--red); overflow: hidden; font-family: "Cabin", sans-serif; }
  .top-panel { position: absolute; left: 22px; top: 22px; right: 22px; height: 290px; background: var(--paper); }
  .blue-panel { position: absolute; left: 0; top: 297px; width: 1200px; height: 903px; background: var(--navy); }
  .blue-panel-inner { position: absolute; left: 22px; top: 0; right: 22px; bottom: 24px; background: radial-gradient(ellipse at 50% 45%, #7dbde6 0%, var(--sky) 55%, var(--sky-deep) 100%); }

  .brand-mark { position: absolute; left: 0; width: 1200px; top: 48px; text-align: center; font-family: "Bebas Neue", sans-serif; color: var(--navy); line-height: 0.9; }
  .brand-mark .line-1 { display: block; font-size: 100px; letter-spacing: 4px; }
  .brand-mark .line-2 { display: block; font-size: 82px; letter-spacing: 2px; }

  .ribbon { position: absolute; left: 0; top: 0; }
  .headline { position: absolute; left: 149px; top: 249px; width: 901px; height: 110px; display: flex; align-items: center; justify-content: center; font-family: "Bebas Neue", sans-serif; font-size: 50px; letter-spacing: 1.5px; color: var(--white); }

  .timeline { position: absolute; left: 0; top: 0; }
  .food-label { position: absolute; width: 190px; margin-left: -95px; text-align: center; color: var(--navy); font-weight: 700; font-size: 27px; line-height: 1.2; letter-spacing: 1px; text-transform: uppercase; }
  .food-label .amount { display: block; font-size: 16px; letter-spacing: 1px; }
  .food-label.wide { width: 240px; margin-left: -120px; }

  .dates { position: absolute; left: 403px; top: 806px; width: 392px; height: 100px; background: var(--navy); color: var(--white); display: flex; align-items: center; justify-content: center; font-weight: 700; font-size: 50px; letter-spacing: 2px; }
  .signup { position: absolute; left: 0; width: 1200px; top: 928px; text-align: center; color: var(--ink); font-weight: 700; font-size: 38px; }
  .url { position: absolute; left: 0; width: 1200px; top: 986px; text-align: center; color: var(--ink); font-weight: 700; font-size: 48px; letter-spacing: 0.5px; }

  .footer { position: absolute; left: 0; top: 1059px; width: 1200px; height: 108px; background: var(--paper); }
  .agency-note { position: absolute; left: 47px; top: 22px; color: var(--navy); font-weight: 500; font-size: 13px; line-height: 1.3; letter-spacing: 0.5px; text-transform: uppercase; }
  .agency-note .abn { display: block; margin-top: 8px; font-weight: 700; font-size: 24px; letter-spacing: 1px; }
  .partner-name { position: absolute; left: 485px; top: 30px; width: 300px; text-align: center; font-family: "Bebas Neue", sans-serif; font-size: 46px; color: var(--red); letter-spacing: 1px; }
</style>
</head>
<body>
<main class="poster">
  <div class="top-panel"></div>
  <div class="blue-panel"><div class="blue-panel-inner"></div></div>

  <div class="brand-mark" aria-label="Meal Pledge">
    <span class="line-1">MEAL</span>
    <span class="line-2">PLEDGE</span>
  </div>

  <svg class="ribbon" width="1200" height="420" viewBox="0 0 1200 420" aria-hidden="true">
    <polygon points="88,297 149,297 149,359 185,393 88,393 125,345" fill="var(--ribbon-tail)"/>
    <polygon points="1112,297 1050,297 1050,359 1014,393 1112,393 1075,345" fill="var(--ribbon-tail)"/>
    <rect x="149" y="249" width="901" height="110" fill="var(--ribbon)"/>
  </svg>
  <h1 class="headline">Could you live on this much food for 1 week?</h1>

  <svg class="timeline" width="1200" height="800" viewBox="0 0 1200 800" aria-hidden="true">
    <g fill="var(--navy)">
      <rect x="19" y="572" width="151" height="36"/>
      <rect x="180" y="572" width="153" height="36"/>
      <rect x="342" y="572" width="152" height="36"/>
      <rect x="505" y="572" width="152" height="36"/>
      <rect x="674" y="572" width="153" height="36"/>
      <rect x="837" y="572" width="153" height="36"/>
      <rect x="1004" y="572" width="152" height="36"/>
    </g>
    <g stroke="var(--navy)" stroke-width="4">
      <line x1="94" y1="590" x2="94" y2="700"/>
      <line x1="256" y1="590" x2="256" y2="480"/>
      <line x1="418" y1="590" x2="418" y2="700"/>
      <line x1="581" y1="590" x2="581" y2="480"/>
      <line x1="750" y1="590" x2="750" y2="700"/>
      <line x1="913" y1="590" x2="913" y2="480"/>
      <line x1="1080" y1="590" x2="1080" y2="700"/>
    </g>
    <g fill="var(--white)" stroke="var(--navy)" stroke-width="3">
      <circle cx="94" cy="590" r="6"/><circle cx="256" cy="590" r="6"/><circle cx="418" cy="590" r="6"/>
      <circle cx="581" cy="590" r="6"/><circle cx="750" cy="590" r="6"/><circle cx="913" cy="590" r="6"/><circle cx="1080" cy="590" r="6"/>
    </g>
    <g fill="var(--navy)">
      <rect x="67" y="703" width="54" height="54" transform="rotate(45 94 730)"/>
      <rect x="229" y="423" width="54" height="54" transform="rotate(45 256 450)"/>
      <rect x="391" y="703" width="54" height="54" transform="rotate(45 418 730)"/>
      <rect x="554" y="423" width="54" height="54" transform="rotate(45 581 450)"/>
      <rect x="723" y="703" width="54" height="54" transform="rotate(45 750 730)"/>
      <rect x="886" y="423" width="54" height="54" transform="rotate(45 913 450)"/>
      <rect x="1053" y="703" width="54" height="54" transform="rotate(45 1080 730)"/>
    </g>
    <g fill="var(--white)" stroke="var(--white)">
      <line x1="84" y1="748" x2="104" y2="712" stroke-width="3"/>
      <line x1="90" y1="748" x2="100" y2="716" stroke-width="3"/>
      <rect x="245" y="437" width="22" height="26" rx="2" stroke="none"/>
      <circle cx="256" cy="452" r="5" fill="var(--navy)" stroke="none"/>
      <g stroke="none">
        <circle cx="410" cy="722" r="3.5"/><circle cx="420" cy="718" r="3.5"/><circle cx="428" cy="727" r="3.5"/>
        <circle cx="414" cy="733" r="3.5"/><circle cx="424" cy="738" r="3.5"/><circle cx="408" cy="742" r="3.5"/>
      </g>
      <ellipse cx="581" cy="450" rx="11" ry="15" stroke="none"/>
      <line x1="581" y1="438" x2="581" y2="462" stroke="var(--navy)" stroke-width="2"/>
      <rect x="739" y="717" width="22" height="28" rx="4" fill="none" stroke-width="3"/>
      <g stroke="none">
        <circle cx="906" cy="444" r="5"/><circle cx="918" cy="442" r="5"/><circle cx="912" cy="454" r="5"/>
        <circle cx="902" cy="456" r="4"/><circle cx="923" cy="453" r="4"/>
      </g>
      <circle cx="1080" cy="736" r="10" stroke="none"/>
      <rect x="1076" y="716" width="8" height="12" stroke="none"/>
    </g>
  </svg>

  <div class="food-label" style="left:94px; top:508px;">Rice<span class="amount">1920g</span></div>
  <div class="food-label" style="left:256px; top:625px;">Flour<span class="amount">400g</span></div>
  <div class="food-label" style="left:418px; top:508px;">Lentils<span class="amount">170g</span></div>
  <div class="food-label wide" style="left:581px; top:625px;">Dried<br>chick peas<span class="amount">85g</span></div>
  <div class="food-label wide" style="left:750px; top:468px;">Tinned<br>sardines<span class="amount">125g</span></div>
  <div class="food-label wide" style="left:913px; top:625px;">Tinned kidney<br>beans<span class="amount">400g</span></div>
  <div class="food-label wide" style="left:1080px; top:472px;">Vegetable<br>oil<span class="amount">300ml</span></div>

  <div class="dates">JUNE 19-25</div>
  <p class="signup">Sign up at</p>
  <p class="url">www.mealpledge.example.org.au</p>

  <footer class="footer">
    <p class="agency-note">The international aid agency of<br>the United Assembly of Parishes.<span class="abn">ABN 17 826 305 419</span></p>
    <p class="partner-name">HOPE BRIDGE</p>
  </footer>
</main>
</body>
</html>
```